Welding company needs a business card

We are looking for a logo and business card.

Contact Information for Business Card

418 Cobblestone Lane
Millbrook, PA 17488
410-555-0173
Rmfabworksco@quorvamail.com

```html
<!DOCTYPE html>
<html lang="en">
<head>
<meta charset="utf-8">
<title>RM Fabworks — Business Card</title>
<link rel="stylesheet" href="https://fonts.googleapis.com/css2?family=Source+Sans+3:wght@400;600&display=swap">
<style>
  :root {
    --backdrop: #ebebeb;
    --card: #f7f7f7;
    --ink: #1f1f1f;
    --brand: #ea7a3c;
    --card-shadow: rgba(0, 0, 0, 0.12);
  }
  * { box-sizing: border-box; margin: 0; padding: 0; }
  html, body {
    width: 1200px;
    height: 800px;
    overflow: hidden;
    background: var(--backdrop);
  }
  .stage {
    width: 1200px;
    height: 800px;
    display: flex;
    align-items: center;
    justify-content: center;
  }
  .business-card {
    position: relative;
    width: 840px;
    height: 480px;
    background: var(--card);
    box-shadow: 0 10px 30px var(--card-shadow);
    display: flex;
    align-items: center;
    font-family: "Source Sans 3", sans-serif;
  }
  .brand {
    width: 48%;
    display: flex;
    align-items: center;
    justify-content: center;
    gap: 14px;
    padding-left: 30px;
    margin-top: -40px;
  }
  .brand-dot {
    width: 34px;
    height: 34px;
    border-radius: 50%;
    background: var(--brand);
    flex: none;
  }
  .brand-name {
    color: var(--brand);
    font-weight: 600;
    font-size: 44px;
    letter-spacing: 0.5px;
    white-space: nowrap;
  }
  .contact {
    width: 52%;
    padding-top: 60px;
    padding-left: 30px;
    list-style: none;
    color: var(--ink);
    font-weight: 400;
    font-size: 26px;
    line-height: 1.2;
    white-space: nowrap;
  }
</style>
</head>
<body>
  <main class="stage">
    <section class="business-card">
      <div class="brand">
        <span class="brand-dot"></span>
        <span class="brand-name">RM Fabworks</span>
      </div>
      <ul class="contact">
        <li class="contact-street">418 Cobblestone Lane</li>
        <li class="contact-city">Millbrook, PA 17488</li>
        <li class="contact-phone">410-555-0173</li>
        <li class="contact-email">Rmfabworksco@quorvamail.com</li>
      </ul>
    </section>
  </main>
</body>
</html>
```